All Natural Mosquito Repellent

My company, BrightFern Company has created an all natural mosquito repellent. I already have other all natural products that I have developed and created labels for. I will include a copy of that label so you have something to work from. I will need two labels. One for the front of the bottle and one for the back. The back label will need space for a UPC. The labels need to be 63mm (H) x 39mm (W)

Target Market(s)

Consumers, Organic, People who like natural products

Font styles to use
Other font styles liked:
• A combination of both Serif and Sans Serif

Requirements
Must have
• Use the words Organic, All Natural, Travel size, made in the USA label
Nice to have
• tag line: Don't beat them off. Spray them away.

```html
<!DOCTYPE html>
<html lang="en">
<head>
<meta charset="utf-8">
<title>BrightFern Co. Mosquito Repellent Labels</title>
<link href="https://fonts.googleapis.com/css2?family=Alfa+Slab+One&family=Libre+Baskerville:ital@1&family=Roboto+Condensed:wght@700&family=Roboto+Slab:wght@600;700;800&display=swap" rel="stylesheet">
<style>
  :root {
    --page: #d9d9dc;
    --label: #3b3b3b;
    --green: #239a6b;
    --white: #ffffff;
    --rule: #7a7a7a;
    --warn-red: #c8242b;
    --badge-navy: #1f3f7c;
    --upc: #ffffff;
  }
  * { margin: 0; padding: 0; box-sizing: border-box; }
  html, body { width: 840px; height: 1200px; overflow: hidden; }
  body { background: var(--page); position: relative; }

  .label-slot { position: absolute; left: 40px; width: 760px; height: 473px; }
  .label-slot--front { top: 90px; }
  .label-slot--back { top: 637px; }

  .label {
    position: absolute; top: 0; left: 0;
    width: 426px; height: 265px;
    background: var(--label);
    transform: scale(1.784);
    transform-origin: top left;
    overflow: hidden;
    color: var(--white);
    font-family: "Roboto Slab", serif;
  }
  .centered { position: absolute; left: 0; right: 0; text-align: center; }

  /* brand line */
  .brand { display: flex; align-items: center; justify-content: center; gap: 6px; position: absolute; left: 0; right: 0; }
  .brand__dot { border-radius: 50%; background: var(--green); flex: none; }
  .brand__name { font-family: "Roboto Slab", serif; font-weight: 700; color: var(--white); white-space: nowrap; }
  .front .brand { top: 44px; }
  .front .brand__dot { width: 24px; height: 24px; }
  .front .brand__name { font-size: 21px; }
  .back .brand { top: 26px; }
  .back .brand__dot { width: 18px; height: 18px; }
  .back .brand__name { font-size: 16px; }

  .rule { position: absolute; height: 1px; background: var(--rule); }

  /* front */
  .front__title {
    position: absolute; left: 50px; top: 78px;
    font-family: "Alfa Slab One", serif; font-size: 54px; line-height: 60px;
    color: var(--green); letter-spacing: 0.5px;
  }
  .front__no-bug { position: absolute; left: 330px; top: 86px; width: 46px; height: 46px; border-radius: 50%; background: var(--warn-red); }
  .front__sub { top: 130px; font-weight: 800; font-size: 28px; line-height: 30px; letter-spacing: 0.5px; }
  .front__organic {
    position: absolute; left: 171px; top: 163px; width: 84px;
    border-top: 1px solid var(--white); border-bottom: 1px solid var(--white);
    text-align: center; font-weight: 700; font-size: 12.5px; line-height: 16px;
  }
  .front__natural-badge { position: absolute; left: 30px; top: 152px; width: 80px; height: 80px; border-radius: 50%; background: var(--green); border: 4px solid var(--white); }
  .front__net-label { top: 204px; font-family: "Roboto Condensed", sans-serif; font-weight: 700; font-size: 9.5px; }
  .front__net-value { top: 213px; font-weight: 700; font-size: 20px; color: var(--green); }
  .front__travel {
    position: absolute; left: 328px; top: 178px; width: 96px; height: 20px;
    background: var(--green); clip-path: polygon(4% 0, 100% 0, 96% 100%, 0 100%);
    font-family: "Roboto Condensed", sans-serif; font-weight: 700; font-size: 11.5px;
    line-height: 20px; text-align: center;
  }
  .front__usa-badge { position: absolute; left: 329px; top: 198px; width: 72px; height: 36px; border-radius: 18px; background: var(--badge-navy); }

  /* back */
  .back__kicker { top: 62px; font-family: "Libre Baskerville", serif; font-style: italic; font-size: 10px; }
  .back__title { top: 70px; font-family: "Alfa Slab One", serif; font-size: 22px; line-height: 28px; }
  .back__sub { top: 96px; font-weight: 800; font-size: 12px; line-height: 14px; }
  .back__copy { position: absolute; left: 38px; width: 350px; text-align: center; font-weight: 600; font-size: 7.4px; line-height: 10px; }
  .back__copy--usage { top: 120px; }
  .back__copy--ingredients { top: 165px; }
  .back__note { position: absolute; left: 34px; top: 212px; width: 176px; font-weight: 600; font-size: 7.4px; line-height: 10px; }
  .back__upc-space { position: absolute; left: 291px; top: 204px; width: 106px; height: 45px; background: var(--upc); }
</style>
</head>
<body>
  <section class="label-slot label-slot--front" aria-label="Front label">
    <div class="label front">
      <div class="brand"><span class="brand__dot"></span><span class="brand__name">BrightFern Co.</span></div>
      <div class="rule" style="left:128px; width:200px; top:76px;"></div>
      <h1 class="front__title">MOSQUIT</h1>
      <div class="front__no-bug" role="img" aria-label="Crossed-out mosquito icon"></div>
      <p class="centered front__sub">REPELLENT</p>
      <p class="front__organic">ORGANIC</p>
      <div class="front__natural-badge" role="img" aria-label="Natural organic badge"></div>
      <p class="centered front__net-label">Net Weight</p>
      <p class="centered front__net-value">125 ml</p>
      <p class="front__travel">Travel size</p>
      <div class="front__usa-badge" role="img" aria-label="Made in USA badge"></div>
    </div>
  </section>

  <section class="label-slot label-slot--back" aria-label="Back label">
    <div class="label back">
      <div class="brand"><span class="brand__dot"></span><span class="brand__name">BrightFern Co.</span></div>
      <div class="rule" style="left:95px; width:236px; top:54px;"></div>
      <p class="centered back__kicker">all natural</p>
      <h2 class="centered back__title">MOSQUITO</h2>
      <p class="centered back__sub">REPELLENT</p>
      <p class="back__copy back__copy--usage">Our all natural mosquito repellent blends plant oils that insects dislike, giving you gentle protection outdoors. Shake well and spray evenly over exposed skin and clothing. Reapply every two hours or after swimming. Keep away from eyes and out of reach of children.</p>
      <p class="back__copy back__copy--ingredients">Ingredients: purified water, witch hazel, citronella oil, lemongrass oil, peppermint oil, cedarwood oil and soybean oil. No DEET, no parabens, no artificial fragrance. Safe for the whole family.</p>
      <p class="back__note">Don't beat them off. Spray them away. Store in a cool, dry place.</p>
      <div class="back__upc-space" aria-label="UPC space"></div>
    </div>
  </section>
</body>
</html>
```